I need double sided standard sized Business Card [3.5" x 2"]
you choose
Professional
Rik Sorensby
Vice President, Director
Suite 2718 - 845 East Linmore Street
Vancouver, B.C. V5R 3K7
rik@halvenminerals.example
www.halvenminerals.example
would like the logo and maybe a colored background

```html
<!DOCTYPE html>
<html lang="en">
<head>
<meta charset="utf-8">
<title>Halven Minerals – Business Cards</title>
<link href="https://fonts.googleapis.com/css2?family=Tinos:wght@400;700&family=Arimo:wght@400;700&display=swap" rel="stylesheet">
<style>
  :root{
    --bg:#e9e6e1;
    --card:#ffffff;
    --navy:#1f4f8f;
    --band:#1c5ea8;
    --band-dark:#154a86;
    --orange:#f29a1d;
    --ink:#2b2b2b;
    --rule:#b9bfc8;
  }
  *{margin:0;padding:0;box-sizing:border-box}
  html,body{width:1200px;height:852px;overflow:hidden;background:var(--bg)}
  .canvas{position:relative;width:1200px;height:852px}
  .card{
    position:absolute;width:540px;height:309px;background:var(--card);
    border-radius:16px;overflow:hidden;box-shadow:0 6px 18px rgba(0,0,0,.18);
    font-family:"Tinos",serif;color:var(--ink)
  }
  .card--front{left:40px;top:272px}
  .card--back{left:620px;top:272px}
  .band{position:absolute;left:0;bottom:0;width:100%;height:50px}
  .wordmark{
    position:absolute;font-family:"Tinos",serif;font-weight:400;color:var(--navy);
    letter-spacing:1px;line-height:1;display:flex;align-items:center;gap:12px
  }
  .wordmark .dot{width:14px;height:14px;border-radius:50%;background:var(--orange)}
  .name{font-family:"Arimo",sans-serif;font-weight:700;color:var(--navy);font-size:17px}
  .title{font-family:"Arimo",sans-serif;font-style:italic;color:var(--orange);font-size:13px;margin-top:3px}
  .address{font-size:15px;line-height:19px;margin-top:9px}
  .divider{position:absolute;width:1px;background:var(--rule)}
  .contacts{list-style:none;font-size:15px;line-height:21px}
  .contacts li{display:flex;align-items:center;gap:8px;white-space:nowrap}
  .contacts svg{width:13px;height:13px;flex:none;fill:none;stroke:var(--navy);stroke-width:2}
  .front-person{position:absolute;right:300px;top:136px;text-align:right}
  .front-contacts{position:absolute;left:262px;top:134px}
  .back-person{position:absolute;left:268px;top:52px}
  .back-contacts{position:absolute;left:268px;top:166px}
</style>
</head>
<body>
<div class="canvas">

  <!-- Front -->
  <section class="card card--front">
    <div class="wordmark" style="left:58px;top:62px;font-size:46px"><span class="dot"></span>Halven</div>

    <div class="front-person">
      <p class="name">Rik Sorensby</p>
      <p class="title">Vice President, Director</p>
      <p class="address">Suite 2718 - 845<br>East Linmore Street<br>Vancouver, B.C. V5R 3K7</p>
    </div>
    <div class="divider" style="left:250px;top:134px;height:100px"></div>
    <ul class="contacts front-contacts">
      <li><svg viewBox="0 0 16 16"><path d="M3 2l3 1 1 3-2 1c1 2 2 3 4 4l1-2 3 1 1 3-2 2C8 15 1 8 1 4z"/></svg>1 855 240 7719</li>
      <li><svg viewBox="0 0 16 16"><path d="M3 2l3 1 1 3-2 1c1 2 2 3 4 4l1-2 3 1 1 3-2 2C8 15 1 8 1 4z"/></svg>(T) 604 240 7719</li>
      <li><svg viewBox="0 0 16 16"><rect x="4" y="1" width="8" height="14" rx="1.5"/><path d="M7 12h2"/></svg>604 555 0142</li>
      <li><svg viewBox="0 0 16 16"><circle cx="8" cy="8" r="3"/><path d="M11 8v1.5a2 2 0 0 0 4 0V8a7 7 0 1 0-3 5.7"/></svg>rik@halvenminerals.example</li>
    </ul>

    <svg class="band" viewBox="0 0 540 50" preserveAspectRatio="none" aria-hidden="true">
      <path d="M0 14 Q270 2 540 10 L540 50 L0 50Z" fill="var(--orange)"/>
      <path d="M0 20 Q270 8 540 16 L540 50 L0 50Z" fill="var(--band)"/>
      <path d="M0 40 Q270 34 540 38 L540 50 L0 50Z" fill="var(--band-dark)"/>
    </svg>
  </section>

  <!-- Back -->
  <section class="card card--back">
    <div class="wordmark" style="left:34px;top:138px;font-size:40px"><span class="dot"></span>Halven</div>

    <div class="divider" style="left:252px;top:48px;height:208px"></div>

    <div class="back-person">
      <p class="name">Rik Sorensby</p>
      <p class="title">Vice President, Director</p>
      <p class="address">Suite 2718 - 845<br>East Linmore Street<br>Vancouver, B.C. V5R 3K7</p>
    </div>
    <ul class="contacts back-contacts">
      <li><svg viewBox="0 0 16 16"><path d="M3 2l3 1 1 3-2 1c1 2 2 3 4 4l1-2 3 1 1 3-2 2C8 15 1 8 1 4z"/></svg>1 855 240 7719</li>
      <li><svg viewBox="0 0 16 16"><path d="M3 2l3 1 1 3-2 1c1 2 2 3 4 4l1-2 3 1 1 3-2 2C8 15 1 8 1 4z"/></svg>(T) 604 240 7719</li>
      <li><svg viewBox="0 0 16 16"><rect x="4" y="1" width="8" height="14" rx="1.5"/><path d="M7 12h2"/></svg>604 555 0142</li>
      <li><svg viewBox="0 0 16 16"><circle cx="8" cy="8" r="3"/><path d="M11 8v1.5a2 2 0 0 0 4 0V8a7 7 0 1 0-3 5.7"/></svg>rik@halvenminerals.example</li>
      <li><svg viewBox="0 0 16 16"><circle cx="8" cy="8" r="6.5"/><path d="M1.5 8h13M8 1.5c-3 3.5-3 9.5 0 13M8 1.5c3 3.5 3 9.5 0 13"/></svg>www.halvenminerals.example</li>
    </ul>

    <svg class="band" viewBox="0 0 540 50" preserveAspectRatio="none" aria-hidden="true">
      <path d="M0 24 Q270 14 540 20 L540 50 L0 50Z" fill="var(--orange)"/>
      <path d="M0 30 Q270 20 540 26 L540 50 L0 50Z" fill="var(--band)"/>
      <path d="M0 44 Q270 38 540 42 L540 50 L0 50Z" fill="var(--band-dark)"/>
    </svg>
  </section>

</div>
</body>
</html>
```